Webbanner-Design für Beteiligungsunternehmen
Zielgruppe
Ich habe ein kleines Familieninternes Beteiligungsunternehmen welches an verschiedenen Firmen beteiligt ist.
Aufgabenstellung
Ich brauche ein Profilbanner für Facebook und Twitter welches zum einen meine Hauptmarke 'Mertlow Holding' und meine Unternehmen an denen ich beteiligt bin (Geldwacht/Kaldoran Real Estate/ TK Holding/Brivalo) zeigt.

```html
<!DOCTYPE html>
<html lang="de">
<head>
<meta charset="utf-8">
<title>Mertlow Holding – Profilbanner</title>
<link rel="stylesheet" href="https://fonts.googleapis.com/css2?family=Michroma&display=swap">
<style>
  :root {
    --page-bg: #ffffff;
    --sky-top: #a9b2c2;
    --sky-mid: #8794b3;
    --haze: #c3c9d6;
    --ridge: #6f7ea3;
    --band: rgba(70, 78, 105, 0.55);
    --ink: #ffffff;
    --shadow: rgba(0, 0, 0, 0.45);
  }
  * { margin: 0; padding: 0; box-sizing: border-box; }
  html, body {
    width: 1200px;
    height: 845px;
    overflow: hidden;
    background: var(--page-bg);
  }
  body { position: relative; font-family: "Michroma", sans-serif; color: var(--ink); }

  .banner {
    position: absolute;
    container-type: inline-size;
    overflow: hidden;
    box-shadow: 0 4px 14px var(--shadow);
  }
  .banner--small { left: 320px; top: 80px; width: 560px; height: 212px; }
  .banner--large { left: 88px; top: 423px; width: 1024px; height: 342px; }

  .banner__scenery {
    position: absolute;
    inset: 0;
    background:
      linear-gradient(180deg,
        var(--sky-top) 0%,
        var(--haze) 12%,
        var(--ridge) 20%,
        var(--sky-mid) 38%,
        var(--haze) 62%,
        var(--sky-mid) 78%,
        var(--ridge) 100%);
  }

  .brand {
    position: absolute;
    left: 50%;
    top: 40%;
    transform: translate(-50%, -50%);
    display: flex;
    align-items: center;
    gap: 1.4cqw;
    white-space: nowrap;
  }
  .brand__square {
    width: 2.6cqw;
    height: 2.6cqw;
    background: var(--ink);
  }
  .brand__name {
    font-size: 3cqw;
    letter-spacing: 0.06em;
    text-transform: uppercase;
  }

  .portfolio {
    position: absolute;
    left: 0;
    right: 0;
    bottom: 0;
    height: 29%;
    background: var(--band);
  }
  .banner--small .portfolio { height: 25%; }

  .portfolio__item {
    position: absolute;
    top: 50%;
    transform: translate(-50%, -50%);
    text-align: center;
    white-space: nowrap;
  }
  .portfolio__item:nth-child(1) { left: 15%; }
  .portfolio__item:nth-child(2) { left: 39%; }
  .portfolio__item:nth-child(3) { left: 61%; }
  .portfolio__item:nth-child(4) { left: 83%; }

  .portfolio__name {
    display: block;
    font-size: 1.6cqw;
    letter-spacing: 0.08em;
    text-transform: uppercase;
  }
  .portfolio__tag {
    display: block;
    margin-top: 0.6cqw;
    font-size: 0.7cqw;
    letter-spacing: 0.4em;
    text-transform: uppercase;
  }
</style>
</head>
<body>

  <section class="banner banner--small" aria-label="Profilbanner Twitter">
    <div class="banner__scenery" role="img" aria-label="Foto: nebelige Berglandschaft in Blaugrau mit fliegendem Vogel"></div>
    <div class="brand">
      <span class="brand__square"></span>
      <span class="brand__name">Mertlow Holding</span>
    </div>
    <div class="portfolio">
      <div class="portfolio__item"><span class="portfolio__name">Geldwacht</span></div>
      <div class="portfolio__item"><span class="portfolio__name">Kaldoran</span><span class="portfolio__tag">Real Estate</span></div>
      <div class="portfolio__item"><span class="portfolio__name">TK Holding</span></div>
      <div class="portfolio__item"><span class="portfolio__name">Brivalo</span><span class="portfolio__tag">Bauunternehmen</span></div>
    </div>
  </section>

  <section class="banner banner--large" aria-label="Profilbanner Facebook">
    <div class="banner__scenery" role="img" aria-label="Foto: nebelige Berglandschaft in Blaugrau mit fliegendem Vogel"></div>
    <div class="brand">
      <span class="brand__square"></span>
      <span class="brand__name">Mertlow Holding</span>
    </div>
    <div class="portfolio">
      <div class="portfolio__item"><span class="portfolio__name">Geldwacht</span></div>
      <div class="portfolio__item"><span class="portfolio__name">Kaldoran</span><span class="portfolio__tag">Real Estate</span></div>
      <div class="portfolio__item"><span class="portfolio__name">TK Holding</span></div>
      <div class="portfolio__item"><span class="portfolio__name">Brivalo</span><span class="portfolio__tag">Bauunternehmen</span></div>
    </div>
  </section>

</body>
</html>
```